Vantrelle Stationary Design

We're seeking a fresh and modern design for our stationery that captures the essence of our Real Estate brand. The current design, while functional, lacks visual appeal. We're looking for a more attractive and engaging design that showcases our professionalism and expertise in the real estate industry. I am attaching the current letter head and an image with a letter "P" as logo.

Target Market(s)

Real Estate Sales and Rentals

Industry/Entity Type

Real Estate

Requirements
Nice to have
• The owner seems to like the letter "P"

```html
<!DOCTYPE html>
<html lang="en">
<head>
<meta charset="utf-8">
<title>Vantrelle Property Solutions – Stationery</title>
<link rel="stylesheet" href="https://fonts.googleapis.com/css2?family=Poppins:wght@400;500;600;700;800&display=swap">
<style>
  :root {
    --stage: #4a4849;
    --navy: #333a68;
    --grey: #7a7a7c;
    --paper: #ffffff;
    --ink: #1d1d22;
  }
  * { box-sizing: border-box; margin: 0; padding: 0; }
  html, body { width: 1200px; height: 2400px; overflow: hidden; }
  body {
    background: var(--stage);
    font-family: "Poppins", sans-serif;
    position: relative;
  }
  .section-title {
    position: absolute; left: 0; width: 1200px; text-align: center; color: #fff;
  }
  .section-title__main {
    top: 106px; font-size: 106px; font-weight: 800; letter-spacing: 0; line-height: 1;
  }
  .section-title__sub {
    top: 210px; font-size: 29px; font-weight: 700; line-height: 1;
  }
  .side-label {
    position: absolute; left: 252px; top: 1929px;
    transform: translate(-50%, -50%) rotate(-90deg);
    color: #fff; font-size: 98px; font-weight: 800; white-space: nowrap; line-height: 1;
  }

  /* Letterhead */
  .letterhead {
    position: absolute; left: 139px; top: 264px; width: 923px; height: 1193px;
    background: var(--paper);
    box-shadow: 10px 14px 22px rgba(0,0,0,.35);
    overflow: hidden;
  }
  .brand { position: absolute; display: flex; align-items: center; gap: 16px; }
  .brand__dot { border-radius: 50%; background: var(--navy); flex: none; }
  .brand__name { font-weight: 600; color: var(--navy); line-height: 1; letter-spacing: -1px; }
  .letterhead .brand { left: 40px; top: 52px; }
  .letterhead .brand__dot { width: 70px; height: 70px; }
  .letterhead .brand__name { font-size: 76px; }
  .letterhead__rule {
    position: absolute; left: 500px; top: 30px; width: 2px; height: 146px; background: var(--navy);
  }
  .contact { color: var(--navy); font-size: 14.5px; line-height: 17px; }
  .contact b { font-weight: 700; }
  .contact .web { font-weight: 600; margin-top: 3px; }
  .contact .address { font-weight: 600; }
  .letterhead .contact { position: absolute; left: 563px; top: 48px; }
  .letterhead .contact .address { position: absolute; left: -3px; top: 75px; white-space: nowrap; }
  .letterhead__wave { position: absolute; left: 0; bottom: 0; width: 923px; height: 168px; }
  .letterhead__footer {
    position: absolute; top: 1152px; left: 0; width: 923px;
    color: #fff; font-size: 10px; font-weight: 700;
  }
  .letterhead__footer span { position: absolute; white-space: nowrap; }

  /* Business cards */
  .card {
    position: absolute; left: 346px; width: 638px; height: 373px;
    box-shadow: 10px 14px 22px rgba(0,0,0,.35);
  }
  .card--front { top: 1544px; background: var(--paper); }
  .card--back { top: 1953px; background: var(--navy); }
  .card--front .brand { left: 26px; top: 52px; gap: 12px; }
  .card--front .brand__dot { width: 60px; height: 60px; }
  .card--front .brand__name { font-size: 60px; }
  .card__name {
    position: absolute; left: 37px; top: 178px;
    font-size: 36px; font-weight: 700; color: var(--navy); line-height: 1;
  }
  .card__role {
    position: absolute; left: 39px; top: 218px; font-size: 17px; color: var(--ink); line-height: 1;
  }
  .card--front .contact {
    position: absolute; left: 41px; top: 265px; font-size: 19px; line-height: 22px;
  }
  .card--front .contact .web { font-size: 14.5px; margin-top: 2px; }
  .card__rule {
    position: absolute; left: 313px; top: 272px; width: 2px; height: 58px; background: var(--navy);
  }
  .card--front .contact.card__address {
    left: 345px; top: 290px; font-size: 16px; line-height: 19px; font-weight: 600;
  }
  .card--back .brand { left: 50%; top: 50%; transform: translate(-50%, -50%); gap: 16px; }
  .card--back .brand__dot { width: 80px; height: 80px; background: #fff; }
  .card--back .brand__name { font-size: 78px; color: #fff; }
</style>
</head>
<body>
  <h1 class="section-title section-title__main">LETTERHEAD</h1>
  <p class="section-title section-title__sub">WITH LOGO AND BUSINESS CARD PREVIEWS</p>

  <section class="letterhead" aria-label="Letterhead">
    <div class="brand">
      <span class="brand__dot"></span>
      <span class="brand__name">Vantrelle</span>
    </div>
    <div class="letterhead__rule"></div>
    <div class="contact">
      <div><b>Phone:</b> 617-555-0148</div>
      <div><b>Fax:</b> 617-555-0193</div>
      <div class="web">Vantrellepropertysolutions.com</div>
      <div class="address">480 Harlow Avenue, Suite 2,<br>Brenton, MA 02199</div>
    </div>
    <svg class="letterhead__wave" viewBox="0 1100 990 180" preserveAspectRatio="none">
      <path d="M0,1117 Q380,1172 750,1130 Q380,1190 0,1143 Z" fill="var(--grey)"/>
      <path d="M0,1160 Q520,1205 990,1107 L990,1280 L0,1280 Z" fill="var(--navy)"/>
    </svg>
    <div class="letterhead__footer">
      <span style="left:75px">VANTRELLE PROPERTY SOLUTIONS</span>
      <span style="left:349px">HOMES WITH HEART</span>
      <span style="left:557px">HELPING BRENTON FAMILIES FIND THE RIGHT PLACE!</span>
    </div>
  </section>

  <div class="side-label">BUSINESS CARD</div>

  <section class="card card--front" aria-label="Business card front">
    <div class="brand">
      <span class="brand__dot"></span>
      <span class="brand__name">Vantrelle</span>
    </div>
    <div class="card__name">Marisa Holt</div>
    <div class="card__role">Managing Director</div>
    <div class="contact">
      <div><b>Phone:</b> 617-555-0148</div>
      <div><b>Fax:</b> 617-555-0193</div>
      <div class="web">Vantrellepropertysolutions.com</div>
    </div>
    <div class="card__rule"></div>
    <div class="contact card__address">480 Harlow Avenue,<br>Suite 2, Brenton, MA 02199</div>
  </section>

  <section class="card card--back" aria-label="Business card back">
    <div class="brand">
      <span class="brand__dot"></span>
      <span class="brand__name">Vantrelle</span>
    </div>
  </section>
</body>
</html>
```